Business and Success Coaching Business Card

Need a business card for my coaching business. I coach small businesses, career professionals and, individuals wanting to unlock their human potential and achieve excellence. At the heart of our methodology is the Shaping Purposeful Action Routines Knowingly (SPARK) approach to formulate empowerment, create principles for success and setting achievable outcomes. I would like something that incorporates our new logo, something clean and sharp with a solid darker, but complementary background, color on the card front. The back should be white where there will be room for three questions

Target Market(s)

People looking to advance and improve themselves through a success coach

Industry/Entity Type

Life Coaching

Contact Information for Business Card

Contact information on card.
Business name on front of card
Questions on back

Font styles to use
Other font styles liked:
• Century Gothic or other Serif style fonts that look similar to Century Gothic

Colors

Designer to choose colors to be used in the design.

Requirements
Must have
• Logo on front of card
• Business name - The Steady Forge
• Contact name - Ted Harlow
• Address - Box 4619, Littleton, CO 80127-4619
• Phone number - 303-555-0147
• Email address - harlow.ted@thesteadyforge.example
• Certifications - CSC, CCHt, PTT, PNLP
• Back of card
• Three questions on the back of the card:
• If you were at your best, what would you do right now?
• What is the decision you have been avoiding?
• What's one action you could take in the next 10 minutes?
Nice to have
• I would like to see a solid color on the front of the card that compliments the logo.
• Back should be white, or could be contrasting, but need to have the three questions.

```html
<!DOCTYPE html>
<html lang="en">
<head>
<meta charset="utf-8">
<title>The Steady Forge – Business Card</title>
<link rel="stylesheet" href="https://fonts.googleapis.com/css2?family=Mulish:wght@700;800&family=Questrial&display=swap">
<style>
  :root {
    --navy: #1f3468;
    --sky: #4a86c8;
    --ink: #2b2b2b;
    --paper: #f5f5f5;
    --backdrop: #cfcfcf;
    --muted: #8a94a6;
    --tagline-light: #c9d6ee;
    --white: #ffffff;
  }
  * { box-sizing: border-box; margin: 0; padding: 0; }
  html, body {
    width: 1200px; height: 834px; overflow: hidden;
    background: var(--backdrop);
    font-family: "Questrial", "Century Gothic", sans-serif;
  }
  .sheet {
    width: 1200px; height: 834px;
    display: flex; align-items: center; justify-content: center; gap: 40px;
  }
  .card {
    position: relative;
    width: 540px; height: 309px;
    overflow: hidden;
    box-shadow: 0 6px 18px rgba(0,0,0,.18);
  }

  /* Contact side */
  .card-contact { background: var(--paper); color: var(--ink); }
  .name-tab {
    position: absolute; left: 0; top: 30px;
    width: 16px; height: 34px; background: var(--sky);
  }
  .identity { position: absolute; left: 30px; top: 30px; }
  .person-name {
    font-family: "Mulish", "Century Gothic", sans-serif;
    font-weight: 800; font-size: 27px; line-height: 1; color: var(--navy);
  }
  .person-name .surname { color: var(--sky); }
  .role { font-size: 15px; margin-top: 6px; }
  .address { position: absolute; left: 30px; top: 118px; font-size: 14px; line-height: 1.45; }
  .contact-list { position: absolute; left: 30px; top: 172px; list-style: none; font-size: 14px; line-height: 1.55; }
  .contact-list li { display: flex; align-items: center; gap: 8px; }
  .contact-list svg { width: 12px; height: 12px; fill: var(--navy); flex: none; }
  .contact-list .web { color: var(--navy); }
  .brand-lockup { position: absolute; text-align: left; }
  .card-contact .brand-lockup { right: 30px; top: 150px; }
  .brand-row { display: flex; align-items: center; gap: 8px; }
  .brand-dot { width: 14px; height: 14px; border-radius: 50%; background: var(--sky); flex: none; }
  .brand-name {
    font-family: "Mulish", "Century Gothic", sans-serif;
    font-weight: 800; font-size: 22px; line-height: 1.1; color: var(--navy);
  }
  .brand-tagline { font-size: 12px; color: var(--muted); margin: 3px 0 0 22px; }
  .credentials {
    position: absolute; right: 34px; bottom: 26px;
    font-size: 17px; letter-spacing: .5px; color: var(--navy);
  }
  .edge-band {
    position: absolute; left: 0; bottom: 0; width: 100%; height: 10px;
    display: flex;
  }
  .edge-band .deep { flex: 0 0 66%; background: var(--navy); }
  .edge-band .light { flex: 1; background: var(--sky); }

  /* Questions side */
  .card-questions { background: var(--navy); color: var(--white); }
  .card-questions .brand-lockup { left: 150px; top: 50px; }
  .card-questions .brand-name { color: var(--white); }
  .card-questions .brand-tagline { color: var(--tagline-light); }
  .question-list {
    position: absolute; left: 26px; top: 128px; list-style: none;
    font-size: 16.5px; line-height: 1.7;
  }
  .question-list li { display: flex; align-items: center; gap: 9px; white-space: nowrap; }
  .question-list li::before {
    content: ""; width: 0; height: 0; flex: none;
    border-left: 9px solid var(--sky);
    border-top: 5px solid transparent; border-bottom: 5px solid transparent;
  }
</style>
</head>
<body>
<main class="sheet">
  <section class="card card-contact" aria-label="Contact side">
    <div class="name-tab"></div>
    <div class="identity">
      <h1 class="person-name">Ted <span class="surname">Harlow</span></h1>
      <p class="role">Director</p>
    </div>
    <p class="address">Box 4619<br>Littleton, CO 80127-4619</p>
    <ul class="contact-list">
      <li><svg viewBox="0 0 12 12"><path d="M3 1l2 2.5-1 1.2a6 6 0 0 0 3.3 3.3l1.2-1L11 9l-1.2 1.8C5.8 11 1 6.2 1.2 2.2z"/></svg>303-555-0147</li>
      <li><svg viewBox="0 0 12 12"><path d="M0 2h12v8H0z M0 2l6 4 6-4" stroke="#f5f5f5" stroke-width="1"/></svg>harlow.ted@thesteadyforge.example</li>
      <li><svg viewBox="0 0 12 12"><circle cx="6" cy="6" r="6"/></svg><span class="web">www.thesteadyforge.example</span></li>
    </ul>
    <div class="brand-lockup">
      <div class="brand-row"><span class="brand-dot"></span><span class="brand-name">The Steady Forge</span></div>
      <p class="brand-tagline">Build your next season</p>
    </div>
    <p class="credentials">CSC, CCHt, PTT, PNLP</p>
    <div class="edge-band"><span class="deep"></span><span class="light"></span></div>
  </section>

  <section class="card card-questions" aria-label="Questions side">
    <div class="brand-lockup">
      <div class="brand-row"><span class="brand-dot"></span><span class="brand-name">The Steady Forge</span></div>
      <p class="brand-tagline">Build your next season</p>
    </div>
    <ul class="question-list">
      <li>If you were at your best, what would you do right now?</li>
      <li>What is the decision you have been avoiding?</li>
      <li>What's one action you could take in the next 10 minutes?</li>
    </ul>
  </section>
</main>
</body>
</html>
```